Industrial Services company needs a business card design

We provide industrial maintenance services including sandblasting, painting, pressure washing, storage tank rehabilitation, and welding. I would like an industrial design that's eye catching. I would like the back-side of the card to list our services.

Industry/Entity Type

Construction

Contact Information for Business Card

address: 418 Hartwell Lane, York, PA 17405
Phone: 410-637-4815
email: corvethinc@mailbrook.net
Daniel Verhoeven, President
www.corvethcoating.net

Logo Text

Corveth Industrial Services

Font styles to use
Sans Serif

Colors
000000
229ed3
0692cd
ffffff

Requirements
Must have
• Easy to read
• our services listed/included on back of card
• eye catching color combinations
Nice to have
• Water storage tank image

```html
<!DOCTYPE html>
<html lang="en">
<head>
<meta charset="utf-8">
<title>Corveth Industrial Services — Business Card</title>
<link rel="stylesheet" href="https://fonts.googleapis.com/css2?family=Fira+Sans:wght@400;500;600&display=swap">
<style>
  :root {
    --ink: #000000;
    --blue: #229ed3;
    --blue-deep: #0692cd;
    --paper: #ffffff;
    --backdrop: #e9e7e3;
  }
  * { box-sizing: border-box; margin: 0; padding: 0; }
  html, body {
    width: 1200px;
    height: 800px;
    overflow: hidden;
    background: var(--backdrop);
    font-family: "Fira Sans", Arial, sans-serif;
  }
  .canvas {
    width: 1200px;
    height: 800px;
    display: flex;
    align-items: center;
    justify-content: center;
    gap: 40px;
  }
  .card {
    position: relative;
    width: 540px;
    height: 309px;
    background: var(--paper);
    box-shadow: 0 2px 10px rgba(0,0,0,0.12);
  }

  /* Back side: services */
  .services-title {
    position: absolute;
    left: 34px;
    top: 110px;
    font-size: 25px;
    font-weight: 400;
    color: var(--ink);
  }
  .services-rule {
    position: absolute;
    left: 34px;
    right: 34px;
    top: 148px;
    border-top: 1.5px solid var(--blue);
  }
  .services-list {
    position: absolute;
    top: 156px;
    list-style: none;
    font-size: 16px;
    line-height: 19px;
    color: var(--blue-deep);
  }
  .services-list--general { left: 210px; }
  .services-list--tanks { left: 360px; }

  /* Front side: contact */
  .contact-name {
    position: absolute;
    left: 40px;
    top: 92px;
    font-size: 24px;
    line-height: 26px;
    color: var(--blue);
    font-weight: 400;
  }
  .contact-name strong { font-weight: 600; }
  .contact-role {
    position: absolute;
    left: 40px;
    top: 120px;
    font-size: 24px;
    line-height: 26px;
    color: var(--ink);
  }
  .contact-rule {
    position: absolute;
    left: 40px;
    right: 22px;
    top: 152px;
    border-top: 1.5px solid var(--blue);
  }
  .contact-details {
    position: absolute;
    left: 40px;
    top: 160px;
    font-style: normal;
    font-size: 15.5px;
    line-height: 19px;
    color: var(--blue-deep);
  }
  .contact-web {
    position: absolute;
    left: 40px;
    top: 228px;
    font-size: 15.5px;
    color: var(--blue-deep);
  }
</style>
</head>
<body>
  <main class="canvas">
    <section class="card card--back" aria-label="Card back: our services">
      <h2 class="services-title">Our Services</h2>
      <div class="services-rule"></div>
      <ul class="services-list services-list--general">
        <li>Sandblasting</li>
        <li>Industrial Painting</li>
        <li>Pressure washing</li>
        <li>Welding</li>
      </ul>
      <ul class="services-list services-list--tanks">
        <li>Storage Tank Inspection</li>
        <li>Maintenance</li>
        <li>Rehabilitation</li>
        <li>Repair &amp;</li>
        <li>Demolition</li>
      </ul>
    </section>

    <section class="card card--front" aria-label="Card front: contact details">
      <h1 class="contact-name"><strong>Daniel</strong> Verhoeven</h1>
      <p class="contact-role">President</p>
      <div class="contact-rule"></div>
      <address class="contact-details">
        418 Hartwell Lane, York, PA 17405<br>
        Phone: 410-637-4815<br>
        email: corvethinc@mailbrook.net
      </address>
      <p class="contact-web">www.corvethcoating.net</p>
    </section>
  </main>
</body>
</html>
```